HollowPine Ventures Inc. Business Card Design

My business is custom renovations and homes.I would need to have a new business logo created to go along with my company name. The business card should be of a modern style as this is the market I am focused on. I would need my contact information and website posted on the card. I would also like to list a few of the tasks I conduct on the card (such as: Renovations, Additions, Repairs, New Homes, Design, Consultations). On the reverse of the card I currently have just my logo and my motto, "Shaping A Bold Path". However, I am open to completely changing everything as I am starting a new year and would like to excel further. Any new ideas and suggestions are always welcomed. Thank you.

Target Market(s)

Upscale residential and commercial renovations and builds

Industry/Entity Type

Business

Contact Information for Business Card

I would like the design to be able to be laser cut or burnt onto a wooden business card. I will be creating one option of cards for really loyal customers (wooden) and a second option for the everyday customer (paper).

Font styles to use
Other font styles liked:
• Calibri / anything of mordern taste

Colors
f37122
5c5c5c
474747
ffffff

Requirements
Must have
• I would like the colours of my business to be a sharp orange and grey. I believe this will symbolize a modern style. I am open to other suggestions if this is not suitable for the designers tastes. My contact info as follows:
• Will Marsh
• President
• HollowPine Ventures Inc.
• 555-214-3987
• will@hollowpineventures.example
• I would like my website (currently under construction) hollowpineventures.example on the card aswell.
Nice to have
• Along with a modern logo representing HollowPine, I would like something on the card besides the logo and contact information. Perhaps a small background design. I feel it may be nice to have my services listed on the card (in smaller font on the bottom) Renovations, Additions, Repairs, Design, Consultations.
Should not have
• The business card should not have too many different colors. Should not have rounded corners.

```html
<!DOCTYPE html>
<html lang="en">
<head>
<meta charset="utf-8">
<title>HollowPine Ventures Inc. Business Card</title>
<link rel="stylesheet" href="https://fonts.googleapis.com/css2?family=Lato:wght@400;700&family=Roboto:wght@400;500&display=swap">
<style>
  :root {
    --orange: #f37122;
    --charcoal: #333333;
    --grey-dark: #474747;
    --grey-mid: #5c5c5c;
    --white: #ffffff;
    --backdrop: #e8e5e1;
  }
  * { margin: 0; padding: 0; box-sizing: border-box; }
  html, body {
    width: 1200px; height: 1000px; overflow: hidden;
    background: var(--backdrop);
    font-family: "Roboto", Arial, sans-serif;
  }
  .canvas { position: relative; width: 1200px; height: 1000px; }

  .card {
    position: absolute; left: 287px; width: 627px; height: 358px;
    box-shadow: 0 4px 14px rgba(0,0,0,0.25);
    overflow: hidden;
  }

  /* Front */
  .card-front { top: 140px; background: var(--charcoal); }
  .front-brand {
    position: absolute; top: 272px; left: 0; right: 0; top: 132px;
    display: flex; align-items: center; justify-content: center; gap: 18px;
  }
  .brand-square { width: 26px; height: 26px; background: var(--orange); }
  .brand-divider { width: 1px; height: 88px; background: var(--white); }
  .front-name {
    font-family: "Lato", Arial, sans-serif; font-weight: 700;
    font-size: 28px; line-height: 34px; color: var(--white);
  }
  .services {
    position: absolute; top: 302px; left: 0; right: 0;
    text-align: center; color: var(--white); font-size: 15px; letter-spacing: 0.2px;
  }
  .services .sep { color: var(--orange); margin: 0 6px; }

  /* Back */
  .card-back { top: 531px; background: var(--white); }
  .back-brand {
    position: absolute; top: 40px; right: 36px;
    font-family: "Lato", Arial, sans-serif; font-weight: 700;
    font-size: 30px; color: var(--orange);
  }
  .holder { position: absolute; left: 35px; top: 170px; }
  .holder-name {
    font-family: "Lato", Arial, sans-serif; font-weight: 700;
    font-size: 19px; color: var(--orange); line-height: 22px;
  }
  .holder-title { font-size: 14px; color: var(--grey-dark); margin-top: 1px; }
  .rule { position: absolute; left: 35px; right: 36px; top: 220px; height: 2px; background: var(--orange); }
  .contacts { position: absolute; left: 35px; top: 236px; list-style: none; }
  .contacts li {
    display: flex; align-items: center; gap: 8px;
    font-size: 14.5px; color: var(--grey-mid); line-height: 20px;
  }
  .contacts svg { width: 11px; height: 11px; fill: var(--orange); }
  .address {
    position: absolute; right: 36px; top: 257px; text-align: right;
    font-size: 14.5px; line-height: 19px; color: var(--grey-mid);
  }
  .footer-bands { position: absolute; left: 0; bottom: 0; width: 627px; height: 24px; }
</style>
</head>
<body>
<main class="canvas">
  <section class="card card-front">
    <div class="front-brand">
      <span class="brand-square"></span>
      <span class="brand-divider"></span>
      <div class="front-name">HollowPine<br>Ventures Inc.</div>
    </div>
    <p class="services">
      Renovations<span class="sep">|</span>Additions<span class="sep">|</span>Repairs<span class="sep">|</span>New Homes<span class="sep">|</span>Consultations
    </p>
  </section>

  <section class="card card-back">
    <div class="back-brand">HollowPine</div>
    <div class="holder">
      <div class="holder-name">Will Marsh</div>
      <div class="holder-title">President</div>
    </div>
    <div class="rule"></div>
    <ul class="contacts">
      <li><svg viewBox="0 0 12 12"><path d="M2.5 0.5 L4.5 0.5 L5.2 3.2 L3.8 4.3 Q5 7 7.7 8.2 L8.8 6.8 L11.5 7.5 L11.5 9.5 Q11.5 11.5 9.5 11.5 Q0.5 10.5 0.5 2.5 Q0.5 0.5 2.5 0.5 Z"/></svg>555-214-3987</li>
      <li><svg viewBox="0 0 12 12"><path d="M0 2 H12 V10 H0 Z M0.8 2.6 L6 6.6 L11.2 2.6" stroke="#fff" stroke-width="0.9"/></svg>will@hollowpineventures.example</li>
      <li><svg viewBox="0 0 12 12"><circle cx="6" cy="6" r="5.5"/><path d="M0.5 6 H11.5 M6 0.5 V11.5 M6 0.5 Q2.5 6 6 11.5 M6 0.5 Q9.5 6 6 11.5" stroke="#fff" stroke-width="0.7" fill="none"/></svg>www.hollowpineventures.example</li>
    </ul>
    <div class="address">Street name, Suite 100<br>State, Zip Code, Country</div>
    <svg class="footer-bands" viewBox="0 0 627 24">
      <rect x="0" y="10" width="300" height="14" fill="var(--grey-dark)"/>
      <polygon points="290,24 313,0 627,0 627,24" fill="var(--orange)"/>
    </svg>
  </section>
</main>
</body>
</html>
```